Business card design for holistic health care clinic

We need a double-sided business card design for our holistic health care clinic that integrates our logo design and also its color scheme. My business is called Veralune. It is an integrative medicine clinic. You have already done the logo for me. Please ensure an elegant and upscale design that is not cluttered, but still has all the necessary information (please see below for details).

Target Market(s)

Wellness, fitness, rehabilitation for educated, well-traveled open-minded clients who are focused on natural, organic, balanced and preventive healthcare and lifestyle.

Industry/Entity Type

Medical

Contact Information for Business Card

Modern, clean.

Number of Pages Required

1 page

Font styles to use
Serif
Sans Serif

Colors

Designer to choose colors to be used in the design.

Requirements
Must have
• Logo on one side, all other information on the other side.
• Other information should include:
• Tobias Wendmere - DOE, CPT, LMT
• 1450 North Calloway Street
• Austin, TX 78744
• 512 555 0184
• 818 555 0127
• info@VeraluneHealth.com
• t.wendmere@VeraluneHealth.com
Nice to have
• Darker background on front - but not totally black - shaded/dark gray.

```html
<!DOCTYPE html>
<html lang="en">
<head>
<meta charset="UTF-8">
<title>Veralune – Business Card</title>
<link href="https://fonts.googleapis.com/css2?family=Lato:wght@400;700;900&display=swap" rel="stylesheet">
<style>
  :root {
    --stage: #2a2a2c;
    --card: #0e0e0f;
    --blue: #1a8fd0;
    --white: #f4f4f4;
    --text: #e9e9e9;
  }
  * { box-sizing: border-box; margin: 0; padding: 0; }
  html, body {
    width: 1200px; height: 1200px; overflow: hidden;
    background: var(--stage);
    font-family: 'Lato', sans-serif;
  }
  .canvas {
    width: 1200px; height: 1200px;
    display: flex; flex-direction: column; align-items: center; justify-content: center;
    gap: 44px;
  }
  .card {
    position: relative;
    width: 900px; height: 514px;
    background: var(--card);
    box-shadow: 0 14px 30px rgba(0,0,0,.55);
    overflow: hidden;
  }
  .accent-rule {
    position: absolute; left: 0; right: 34px; bottom: 62px;
    display: flex; gap: 6px; height: 4px;
  }
  .accent-rule .rule-white { flex: 1; background: var(--white); }
  .accent-rule .rule-blue { flex: 1.05; background: var(--blue); }

  .brand { color: var(--blue); text-align: center; }
  .brand-name {
    font-weight: 900; text-transform: uppercase; line-height: 1;
    letter-spacing: 2px;
  }
  .brand-tagline { font-weight: 700; letter-spacing: .5px; margin-top: 6px; }

  /* front */
  .card-front .brand {
    position: absolute; left: 0; right: 0; top: 150px;
  }
  .card-front .brand-name { font-size: 104px; }
  .card-front .brand-tagline { font-size: 30px; }

  /* back */
  .card-back .brand {
    position: absolute; left: 40px; width: 410px; top: 190px;
  }
  .card-back .brand-name { font-size: 74px; }
  .card-back .brand-tagline { font-size: 22px; }
  .divider {
    position: absolute; left: 470px; top: 105px; width: 2px; height: 270px;
    background: var(--blue);
  }
  .contact { position: absolute; left: 505px; top: 110px; color: var(--text); }
  .contact-name { font-size: 23px; font-weight: 900; color: var(--white); text-transform: uppercase; }
  .contact-name .credentials { color: var(--blue); }
  .contact-address { font-size: 21px; line-height: 1.3; margin-top: 16px; }
  .contact-list { list-style: none; margin-top: 20px; }
  .contact-list li { display: flex; align-items: center; gap: 14px; font-size: 21px; height: 38px; }
  .contact-list svg { width: 22px; height: 22px; flex: none; fill: none; stroke: var(--blue); stroke-width: 2; }
</style>
</head>
<body>
<main class="canvas">
  <section class="card card-front">
    <div class="brand">
      <div class="brand-name">Veralune</div>
      <div class="brand-tagline">Integrative Holistic Medicine</div>
    </div>
    <div class="accent-rule"><span class="rule-white"></span><span class="rule-blue"></span></div>
  </section>

  <section class="card card-back">
    <div class="brand">
      <div class="brand-name">Veralune</div>
      <div class="brand-tagline">Integrative Holistic Medicine</div>
    </div>
    <div class="divider"></div>
    <div class="contact">
      <p class="contact-name">Tobias Wendmere - <span class="credentials">DOE, CPT, LMT</span></p>
      <p class="contact-address">1450 North Calloway Street<br>Austin, TX 78744</p>
      <ul class="contact-list">
        <li>
          <svg viewBox="0 0 24 24"><path d="M3 9c0-3 4-5 9-5s9 2 9 5l-3 1-2-3H8L6 10z" fill="var(--blue)"/><rect x="6" y="12" width="12" height="8" rx="1" fill="var(--blue)"/></svg>
          512 555 0184
        </li>
        <li>
          <svg viewBox="0 0 24 24"><rect x="3" y="5" width="18" height="14" rx="2"/><line x1="7" y1="16" x2="17" y2="16"/></svg>
          818 555 0127
        </li>
        <li>
          <svg viewBox="0 0 24 24"><rect x="3" y="6" width="18" height="12"/><path d="M3 6l9 7 9-7"/></svg>
          info@VeraluneHealth.com
        </li>
        <li>
          <svg viewBox="0 0 24 24"><circle cx="12" cy="12" r="9"/><ellipse cx="12" cy="12" rx="4" ry="9"/><line x1="3" y1="12" x2="21" y2="12"/></svg>
          t.wendmere@VeraluneHealth.com
        </li>
      </ul>
    </div>
    <div class="accent-rule"><span class="rule-white"></span><span class="rule-blue"></span></div>
  </section>
</main>
</body>
</html>
```